Cutting Edge Property Services Provider is Looking to Update Business Card Design

We are looking to freshen up our business cards to match our cutting edge technology based image.

QUARVO-LYN - Where Service Meets Technology

More information about our company can be found on our website at www.quarvo-lyn.example

We integrate technology in a historically low tech industry.

We have appeared on the Brisk 300/3000 list 2 years in a row and we're previously recognized as the 5th Fastest Growing Company in San Diego.

Our core colors are blue and white, but are not against accents that might improve our image.

We currently have our Mission Statement on our Business Cards in a folding design:
QUARVO-LYN IS A FORWARD-THINKING FACILITY PARTNER. BY PAIRING SMART SYSTEMS WITH PRACTICAL METHODS THAT RAISE PRODUCTIVITY ACROSS EVERY SITE, WE DELIVER DEPENDABLE RESULTS FOR EVERY PROPERTY. BUILDING TRUSTED PARTNERSHIPS WITH OUR CUSTOMERS AND TEAMS IS THE FOUNDATION OF EVERYTHING WE DO.

We'd like to convey the image of a cutting edge, technology based company. Want the cards to pop.

Target Market(s)

Commercial Property Managers - 20 to 50 year old professionals

Industry/Entity Type

Business

Requirements
Must have
• Must utilize our logo obviously, but are definitely open to using variations on the logo. Utilizing the components of the logo, but maybe in different configurations or backgrounds, etc...

Must use the Name: QUARVO-LYN.
Can also use QUARVO-LYN PROPERTY SERVICES.

Must include the Mission Statement

Must say: Where Care Runs On Innovation
Nice to have
• We are considering plastic stock, shaped cards, or folding cards.

Nothing over the top or really expensive, but will consider if it conveys innovation and technology.
Should not have
• No images of toilets, buildings, trees, or anything relating to commercial properties.

We want to convey our technology image.

```html
<!DOCTYPE html>
<html lang="en">
<head>
<meta charset="utf-8">
<title>QUARVO-LYN Folding Business Card</title>
<link rel="stylesheet" href="https://fonts.googleapis.com/css2?family=Open+Sans:wght@400;600;700;800&display=swap">
<style>
  :root {
    --brand-blue: #0b4a7e;
    --brand-blue-deep: #08406f;
    --paper: #ffffff;
    --backdrop: #3a2a20;
    --label-red: #e8232a;
    --ink-grey: #444a52;
    --rule-grey: #c9ccd0;
  }
  * { box-sizing: border-box; margin: 0; padding: 0; }
  html, body { width: 1200px; height: 802px; overflow: hidden; }
  body {
    position: relative;
    background: var(--backdrop);
    font-family: "Open Sans", Arial, sans-serif;
  }
  .panel-label {
    position: absolute;
    width: 546px;
    text-align: center;
    color: var(--label-red);
    font-weight: 700;
    font-size: 33px;
    letter-spacing: 5px;
  }
  .card {
    position: absolute;
    width: 546px;
    height: 311px;
    overflow: hidden;
  }
  .card--inner-top { left: 45px; top: 72px; background: var(--paper); border-radius: 26px; }
  .card--front { left: 619px; top: 72px; background: var(--paper); }
  .card--inner-bottom { left: 45px; top: 403px; background: var(--brand-blue); }
  .card--back { left: 619px; top: 403px; }

  .wordmark {
    position: absolute;
    left: 0; right: 0;
    display: flex;
    align-items: center;
    justify-content: center;
    gap: 14px;
    color: var(--brand-blue);
    font-weight: 800;
    white-space: nowrap;
  }
  .wordmark__square { background: var(--brand-blue); flex: none; }

  .card--inner-top .wordmark { top: 110px; font-size: 40px; }
  .card--inner-top .wordmark__square { width: 44px; height: 44px; }
  .inner-top__url {
    position: absolute; left: 0; right: 0; top: 264px;
    text-align: center; font-size: 19px; letter-spacing: 3px; color: #222;
  }

  .card--front .wordmark { top: 70px; font-size: 30px; }
  .card--front .wordmark__square { width: 34px; height: 34px; }
  .front__identity {
    position: absolute; left: 80px; top: 198px; width: 148px;
    text-align: right; color: var(--brand-blue);
  }
  .front__name { font-size: 21px; line-height: 26px; }
  .front__title { font-size: 14px; color: var(--ink-grey); }
  .front__divider {
    position: absolute; left: 240px; top: 195px; width: 1px; height: 60px; background: var(--rule-grey);
  }
  .front__contacts {
    position: absolute; left: 268px; top: 193px; list-style: none;
    font-size: 14.5px; color: #222; line-height: 21px;
  }
  .front__contacts li { display: flex; align-items: center; gap: 6px; }
  .front__contacts svg { width: 11px; height: 11px; fill: var(--brand-blue-deep); }
  .front__rule { position: absolute; left: 0; right: 0; top: 271px; height: 2px; background: var(--rule-grey); }
  .front__address {
    position: absolute; left: 0; right: 0; bottom: 0; height: 33px;
    background: var(--brand-blue); color: var(--paper);
    font-size: 14px; text-align: center; line-height: 33px;
  }

  .mission {
    position: absolute; left: 24px; right: 24px; top: 63px;
    text-align: center; color: var(--paper);
    font-size: 15px; line-height: 30.5px; text-transform: uppercase;
    white-space: nowrap;
  }

  .back__pattern {
    position: absolute; inset: 0;
    background: radial-gradient(circle at 50% 50%, #0f5288 0%, var(--brand-blue-deep) 80%);
  }
  .card--back .wordmark { top: 110px; color: var(--paper); font-size: 46px; }
  .back__tagline {
    position: absolute; left: 0; right: 0; top: 231px;
    text-align: center; color: var(--paper); font-weight: 700; font-size: 22px;
  }
</style>
</head>
<body>
  <div class="panel-label" style="left:45px; top:12px;">Inner Top</div>
  <div class="panel-label" style="left:619px; top:12px;">Front</div>
  <div class="panel-label" style="left:45px; top:726px;">Inner Bottom</div>
  <div class="panel-label" style="left:619px; top:726px;">Back</div>

  <section class="card card--inner-top">
    <div class="wordmark"><span class="wordmark__square"></span>QUARVO-LYN</div>
    <p class="inner-top__url">www.quarvo-lyn.example</p>
  </section>

  <section class="card card--front">
    <div class="wordmark"><span class="wordmark__square"></span>QUARVO-LYN</div>
    <div class="front__identity">
      <p class="front__name">Your Name</p>
      <p class="front__title">Title</p>
    </div>
    <div class="front__divider"></div>
    <ul class="front__contacts">
      <li><svg viewBox="0 0 12 12"><path d="M2.5 1l2 2.5-1 1.2a7 7 0 0 0 3.8 3.8l1.2-1 2.5 2-1 1.5C5.5 11 1 6.5.9 2z"/></svg>1(800) 555-0142</li>
      <li><svg viewBox="0 0 12 12"><path d="M0 3h12v7H0zM0 3l6 4 6-4" stroke="#fff" stroke-width=".8"/></svg>info@quarvo-lyn.example</li>
      <li><svg viewBox="0 0 12 12"><circle cx="6" cy="6" r="5.5"/><path d="M.5 6h11M6 .5v11" stroke="#fff" stroke-width=".8"/></svg>www.quarvo-lyn.example</li>
    </ul>
    <div class="front__rule"></div>
    <p class="front__address">1250 Harbor Crest Way, Suite 210, Brookvale, CA 90000</p>
  </section>

  <section class="card card--inner-bottom">
    <p class="mission">QUARVO-LYN is a forward-thinking facility partner.<br>By pairing smart systems with practical methods that<br>raise productivity across every site, we deliver<br>dependable results for every property. Building<br>trusted partnerships with our customers and teams<br>is the foundation of everything we do.</p>
  </section>

  <section class="card card--back">
    <div class="back__pattern" role="img" aria-label="Repeating brand pattern in deep blue tones"></div>
    <div class="wordmark">QUARVO-LYN</div>
    <p class="back__tagline">Where Care Runs On Innovation</p>
  </section>
</body>
</html>
```